Business card design needed

We are a Custom Joinery and specialise in design, Manufacture and Installation of kitchens and cabinetry
We currently have a logo based on the northern star in red and black but are open to something that would look fresh and clean
Updates

Project Deadline Extended
Reason: Need a couple days to go through designs. Finding some designs that are great on front and others great on reverse. I would like to be able to comment and get the total look we are after.

Target Market(s)

30-50 year olds who are looking to renovate

Industry/Entity Type

Business

Contact Information for Business Card

Larchfield Fitouts
ABN 37 418 260 573
Colin Pratley - Cabinetmaker/Designer Licence No. 318570K

Requirements
Nice to have
• Maybe a nice fresh modern kitchen picture

```html
<!DOCTYPE html>
<html lang="en">
<head>
<meta charset="utf-8">
<title>Larchfield Fitouts – Business Card</title>
<link href="https://fonts.googleapis.com/css2?family=Open+Sans:wght@400;600;700&display=swap" rel="stylesheet">
<style>
  :root {
    --backdrop: #e4e4e4;
    --card: #fbfbfb;
    --ink: #262626;
    --ink-soft: #555555;
    --red: #d2141d;
    --charcoal: #353535;
    --photo-a: #8d8a78;
    --photo-b: #c9cbc2;
    --photo-c: #6f6a5c;
  }
  * { box-sizing: border-box; margin: 0; padding: 0; }
  html, body {
    width: 1200px; height: 800px; overflow: hidden;
    background: var(--backdrop);
    font-family: "Open Sans", Arial, sans-serif;
  }
  .stage {
    position: relative; width: 1200px; height: 800px;
  }
  .card {
    position: absolute; top: 245px;
    width: 540px; height: 309px;
    background: var(--card);
    box-shadow: 0 6px 18px rgba(0,0,0,0.18);
    overflow: hidden;
  }
  .card--front { left: 40px; }
  .card--back { left: 620px; }

  /* Front */
  .kitchen-photo {
    position: absolute; left: 0; top: 0; width: 150px; height: 100%;
    background: linear-gradient(170deg, var(--photo-a) 0%, var(--photo-b) 45%, var(--photo-c) 100%);
  }
  .divider-band {
    position: absolute; left: 150px; top: 0; width: 18px; height: 100%;
    background: var(--charcoal);
  }
  .brand {
    position: absolute; display: flex; align-items: center; gap: 10px;
  }
  .brand__mark {
    width: 14px; height: 14px; background: var(--red); flex: none;
  }
  .brand__name {
    color: var(--ink); font-weight: 400; text-transform: uppercase;
    line-height: 1.05; letter-spacing: 0.5px;
  }
  .card--front .brand { left: 270px; top: 78px; }
  .card--front .brand__name { font-size: 24px; }
  .contact {
    position: absolute; right: 32px; bottom: 28px; text-align: right;
  }
  .contact__name {
    font-size: 15px; font-weight: 700; color: #3a3a3a; letter-spacing: 0.6px;
    text-transform: uppercase;
  }
  .contact__company { font-size: 14px; color: var(--red); margin-bottom: 8px; }
  .contact__detail { font-size: 13px; color: var(--ink-soft); line-height: 1.4; }

  /* Back */
  .card--back .brand { left: 205px; top: 62px; }
  .card--back .brand__name { font-size: 28px; }
  .rule-line {
    position: absolute; left: 0; top: 204px; width: 100%; height: 4px;
    background: var(--charcoal);
  }
  .web-band {
    position: absolute; left: 0; top: 214px; width: 100%; height: 34px;
    background: var(--red);
    display: flex; align-items: center; gap: 8px; padding-left: 22px;
  }
  .web-band__dot {
    width: 14px; height: 14px; border-radius: 50%; background: #fff; flex: none;
  }
  .web-band__url { color: #fff; font-size: 12px; letter-spacing: 0.3px; }
</style>
</head>
<body>
<div class="stage">
  <section class="card card--front">
    <div class="kitchen-photo" role="img" aria-label="Photo of a modern kitchen with olive cabinets, a steel sink and white benchtop"></div>
    <div class="divider-band"></div>
    <div class="brand">
      <span class="brand__mark"></span>
      <span class="brand__name">Larchfield<br>Fitouts</span>
    </div>
    <div class="contact">
      <p class="contact__name">Colin Pratley</p>
      <p class="contact__company">Larchfield Fitouts</p>
      <p class="contact__detail">ABN 37 418 260 573</p>
      <p class="contact__detail">Cabinetmaker/Designer Licence No. 318570K</p>
    </div>
  </section>

  <section class="card card--back">
    <div class="brand">
      <span class="brand__mark"></span>
      <span class="brand__name">Larchfield<br>Fitouts</span>
    </div>
    <div class="rule-line"></div>
    <div class="web-band">
      <span class="web-band__dot"></span>
      <span class="web-band__url">www.larchfieldfitouts.com</span>
    </div>
  </section>
</div>
</body>
</html>
```